Help design website for "Verdant Harbor Advisory" to advance the common good

Here is the Google doc link that lays out the design:

https://files.quillmarsh.net/doc/7TrWbnQe48XkLpZa2uMvYcD0sHfGjR35NwoEi9KxyBt/view?mode=share

Here is the Google drive folder with the logos and photos: https://store.quillmarsh.net/open?id=4K9pRtLmWqZx8825BvNcUaYeHs3Jd

The testimonials are being gathered and will be shared by Friday, 1/4.

The winner will also have to migrate the coding files to my hosting site.

Thank you for your help! Looking forward to seeing your designs.

Target Market(s)

Prospective clients

Industry/Entity Type

Non Profit

Coding

Coded - Design and coding required

Number of Pages Required

5+ page

Requirements
Must have
• Noted in the Google doc regarding layout.
Nice to have

```html
<!DOCTYPE html>
<html lang="en">
<head>
<meta charset="utf-8">
<title>Verdant Harbor Advisory</title>
<link href="https://fonts.googleapis.com/css2?family=Open+Sans:wght@400;600;700&family=Raleway:wght@500;600&display=swap" rel="stylesheet">
<style>
  :root {
    --backdrop: #c9cacd;
    --navy: #2e3342;
    --navy-deep: #262a37;
    --accent: #2f9fdc;
    --accent-soft: #4aaee6;
    --white: #ffffff;
    --ink: #3b3f48;
    --muted: #7b808a;
    --rule: #d6d9de;
  }
  * { box-sizing: border-box; margin: 0; padding: 0; }
  html, body { width: 710px; height: 1200px; overflow: hidden; background: var(--backdrop); }
  body { font-family: "Open Sans", Arial, sans-serif; color: var(--ink); position: relative; }

  .page {
    position: absolute; left: 85px; top: 36px; width: 538px; height: 1126px;
    background: var(--white); overflow: hidden;
  }

  /* navigation */
  .site-nav {
    height: 46px; background: var(--navy); display: flex; align-items: center;
    justify-content: space-between; padding: 0 18px 0 20px;
  }
  .nav-links { display: flex; gap: 14px; list-style: none; }
  .nav-links a {
    font-size: 6.5px; font-weight: 600; letter-spacing: .6px; color: #cfd3da;
    text-decoration: none; text-transform: uppercase;
  }
  .nav-links a.current { color: var(--accent-soft); border-bottom: 1px solid var(--accent-soft); padding-bottom: 2px; }
  .brand { display: flex; align-items: center; gap: 6px; }
  .brand-dot { width: 12px; height: 12px; border-radius: 50%; background: var(--accent); }
  .brand-name {
    font-size: 6.5px; font-weight: 600; color: #cfd3da; text-transform: uppercase;
    letter-spacing: .6px; line-height: 1.2; width: 82px;
  }

  /* hero */
  .hero { position: relative; height: 214px; }
  .hero-photo {
    position: absolute; inset: 0;
    background: linear-gradient(180deg, #e6e8ec 0%, #cfd3da 45%, #4a4f5c 80%, #2c303b 100%);
  }
  .hero-copy { position: absolute; left: 0; right: 0; top: 122px; text-align: center; }
  .hero-title { font-family: "Raleway", "Open Sans", sans-serif; font-weight: 600; font-size: 25px; color: var(--white); }
  .hero-sub { font-size: 9px; color: var(--accent-soft); margin-top: 1px; }
  .hero-button {
    display: inline-block; margin-top: 6px; padding: 3px 14px; background: var(--accent);
    color: var(--white); font-size: 6.5px; font-weight: 700; letter-spacing: .8px;
  }
  .hero-curve { position: absolute; left: 0; bottom: -1px; width: 538px; height: 34px; }

  /* section headers */
  .section-head { text-align: center; }
  .section-mark { display: block; margin: 0 auto 4px; }
  .section-title {
    font-family: "Raleway", "Open Sans", sans-serif; font-weight: 500; font-size: 17px;
    letter-spacing: 1.5px; color: var(--ink);
  }

  .about { padding-top: 44px; }
  .about-lead {
    width: 380px; margin: 16px auto 0; text-align: center; color: var(--accent);
    font-size: 11.5px; font-weight: 600; line-height: 1.45;
  }
  .about-body { display: flex; gap: 16px; width: 400px; margin: 18px auto 0; align-items: flex-start; }
  .founder-photo {
    flex: 0 0 118px; height: 118px; border-radius: 50%; margin-top: 8px;
    background: radial-gradient(circle at 50% 40%, #c9b7a6 0%, #8d8079 55%, #4d4b52 100%);
  }
  .about-text p { font-size: 6.6px; line-height: 1.65; color: var(--muted); margin-bottom: 8px; }

  .work { margin-top: 34px; }
  .divider { display: flex; align-items: center; justify-content: center; gap: 8px; margin-bottom: 8px; }
  .divider span { width: 210px; height: 1px; background: var(--rule); }

  .work-band { background: var(--accent); margin-top: 12px; height: 330px; padding: 22px 0 0; }
  .client-grid {
    display: grid; grid-template-columns: repeat(3, 118px); gap: 40px 36px;
    justify-content: center;
  }
  .client-card {
    height: 118px; background: var(--white); display: flex; flex-direction: column;
    align-items: center; justify-content: flex-end; padding: 0 8px 12px; text-align: center;
  }
  .client-mark { display: flex; align-items: center; gap: 4px; margin-bottom: auto; margin-top: 26px; }
  .client-mark i { width: 14px; height: 14px; background: var(--navy); display: block; }
  .client-mark b { font-size: 8px; font-weight: 700; color: var(--navy); }
  .client-name { font-size: 6.2px; color: var(--accent); line-height: 1.35; }

  .site-footer {
    position: absolute; left: 0; right: 0; bottom: 0; height: 86px; background: var(--navy-deep);
    display: flex; flex-direction: column; align-items: center; justify-content: center; gap: 12px;
  }
  .social { display: flex; gap: 14px; list-style: none; }
  .social li { width: 17px; height: 17px; border: 1.3px solid #c6cad2; border-radius: 50%; }
  .copyright { font-size: 6.5px; letter-spacing: 1px; color: #aeb3bc; text-transform: uppercase; }
</style>
</head>
<body>
<div class="page">
  <header class="site-nav">
    <ul class="nav-links">
      <li><a class="current" href="#about">About</a></li>
      <li><a href="#services">Services &amp; Testimonials</a></li>
      <li><a href="#media">Media &amp; Impact</a></li>
      <li><a href="#contact">Contact</a></li>
    </ul>
    <div class="brand">
      <span class="brand-dot"></span>
      <span class="brand-name">Verdant Harbor Advisory</span>
    </div>
  </header>

  <section class="hero">
    <div class="hero-photo" role="img" aria-label="Team of smiling consultants in business attire standing in a bright office"></div>
    <div class="hero-copy">
      <h1 class="hero-title">We'll get it done</h1>
      <p class="hero-sub">for your mission and community</p>
      <span class="hero-button">MORE</span>
    </div>
    <svg class="hero-curve" viewBox="0 0 538 34" aria-hidden="true">
      <path d="M0 34 L0 20 Q269 -8 538 20 L538 34 Z" fill="#ffffff"/>
      <circle cx="269" cy="12" r="5" fill="none" stroke="#b9bec6" stroke-width="1"/>
    </svg>
  </section>

  <section class="about" id="about">
    <div class="section-head">
      <svg class="section-mark" width="22" height="10" viewBox="0 0 22 10" aria-hidden="true">
        <line x1="0" y1="5" x2="7" y2="5" stroke="#b9bec6"/><circle cx="11" cy="5" r="3" fill="none" stroke="#b9bec6"/><line x1="15" y1="5" x2="22" y2="5" stroke="#b9bec6"/>
      </svg>
      <h2 class="section-title">ABOUT</h2>
    </div>
    <p class="about-lead">Verdant Harbor Advisory supports nonprofit organizations and educational institutions to carry out their missions to benefit the wider community.</p>
    <div class="about-body">
      <div class="founder-photo" role="img" aria-label="Portrait of the founder"></div>
      <div class="about-text">
        <p>Founder Ana Rivera is an educator with a 20 year record of demonstrated achievement and leadership roles in nonprofit and educational institutions. Most recently she served as Associate Dean of Students at a research university, where she designed, implemented and evaluated programs. She partners with organizations to create positive outcomes and builds strategic, data-informed plans for growth, outreach and communication.</p>
        <p>Ana is a native of the coast and has also lived in several cities across the country and abroad. She earned her bachelor's degree in social studies and her master's degree in education, and she speaks three languages.</p>
      </div>
    </div>
  </section>

  <section class="work">
    <div class="divider"><span></span>
      <svg width="12" height="12" viewBox="0 0 12 12" aria-hidden="true"><circle cx="6" cy="6" r="4" fill="none" stroke="#b9bec6"/></svg>
      <span></span></div>
    <div class="section-head"><h2 class="section-title">WORK HISTORY</h2></div>
    <div class="work-band">
      <div class="client-grid">
        <div class="client-card"><div class="client-mark"><i></i><b>Lakeview</b></div><p class="client-name">Lakeview University Community Service Center</p></div>
        <div class="client-card"><div class="client-mark"><i></i><b>Meridian</b></div><p class="client-name">Meridian Center for Civic Leadership</p></div>
        <div class="client-card"><div class="client-mark"><i></i><b>Northstar</b></div><p class="client-name">Northstar Bay Area Public Schools</p></div>
        <div class="client-card"><div class="client-mark"><i></i><b>Schools</b></div><p class="client-name">Other Schools</p></div>
        <div class="client-card"><div class="client-mark"><i></i><b>CivicServe</b></div><p class="client-name">CivicServe Fellows</p></div>
        <div class="client-card"><div class="client-mark"><i></i><b>Pacific</b></div><p class="client-name">Pacific Exchange and Teaching Programme</p></div>
      </div>
    </div>
  </section>

  <footer class="site-footer" id="contact">
    <ul class="social"><li></li><li></li><li></li><li></li></ul>
    <p class="copyright">Verdant Harbor Advisory © 2019</p>
  </footer>
</div>
</body>
</html>
```